Real Estate Managemene Company Needs Business Card Design

We have a logo design and just need business cards made now for our business. Please use PDF logo # 3.

Card with Information to be attached shortly.

The card is used for a real estate management company. We will need to add four other employees and their cards.

Industry/Entity Type

Real Estate

Contact Information for Business Card

Tariq Hamdan
President
3187 Thornwick Avenue
Suite C
Harlow Springs, WI 60152
Phone 630.417.2286
Fax 630.417.2287
Cell 630.473.8062
vantorp@mailbreeze.net

Once design is approved we will have four other employees
Omar Hamdan
Operations Manager

Nadia Hamdan
Administrative Manager

Faz Hamdan
Principal

We would need to take out the cell # 630.473.8062 out for the remaining three cards.

Requirements
Must have
• Please use logo attached

```html
<!DOCTYPE html>
<html lang="en">
<head>
<meta charset="utf-8">
<title>Northvale Realty Management Corporation – Business Card</title>
<link rel="stylesheet" href="https://fonts.googleapis.com/css2?family=Crimson+Text:wght@400;600&display=swap">
<style>
  :root {
    --stage-top: #ffffff;
    --stage-bottom: #c2c1c2;
    --blue-light: #0a79b9;
    --blue-mid: #0a6fae;
    --blue-deep: #0c4c88;
    --ink-white: #ffffff;
    --band-white: #f7f8fa;
    --band-shadow: #dcdee3;
    --email-ink: #1b4f8c;
  }
  * { margin: 0; padding: 0; box-sizing: border-box; }
  html, body { width: 1200px; height: 790px; overflow: hidden; }
  body {
    background: linear-gradient(to bottom, var(--stage-top) 0%, var(--stage-bottom) 100%);
    font-family: "Crimson Text", Georgia, serif;
    position: relative;
  }
  .card-shapes { position: absolute; left: 0; top: 0; }
  .text { position: absolute; transform: translateX(-50%); white-space: nowrap; text-align: center; color: var(--ink-white); }

  .company-name {
    left: 613px; top: 280px;
    font-weight: 600; font-size: 42px; letter-spacing: 1.5px; line-height: 1;
    font-variant: small-caps;
  }
  .company-sub {
    left: 613px; top: 318px;
    font-weight: 600; font-size: 15.5px; letter-spacing: 0.6px; line-height: 1;
    font-variant: small-caps;
  }

  .person-name { left: 608px; top: 479px; font-weight: 600; font-size: 34px; line-height: 1; }
  .person-title { left: 608px; top: 512px; font-weight: 400; font-size: 14px; line-height: 1; letter-spacing: 0.3px; }

  .contact-block { font-size: 10.5px; line-height: 11.3px; font-weight: 400; }
  .address { left: 614px; top: 553px; }
  .phones { left: 614px; top: 598px; }

  .email { left: 614px; top: 658px; color: var(--email-ink); font-size: 12.5px; font-weight: 600; line-height: 1; }
</style>
</head>
<body>
  <svg class="card-shapes" width="1200" height="790" viewBox="0 0 1200 790" aria-hidden="true">
    <defs>
      <linearGradient id="front-fill" x1="0" y1="0" x2="0" y2="1">
        <stop offset="0" stop-color="var(--blue-light)"/>
        <stop offset="0.8" stop-color="var(--blue-mid)"/>
        <stop offset="1" stop-color="var(--blue-deep)"/>
      </linearGradient>
      <linearGradient id="back-fill" x1="0" y1="0" x2="0" y2="1">
        <stop offset="0" stop-color="var(--blue-deep)"/>
        <stop offset="0.45" stop-color="var(--blue-mid)"/>
        <stop offset="1" stop-color="var(--blue-light)"/>
      </linearGradient>
      <linearGradient id="band-fill" x1="0" y1="0" x2="0" y2="1">
        <stop offset="0" stop-color="var(--band-white)"/>
        <stop offset="1" stop-color="var(--band-shadow)"/>
      </linearGradient>
    </defs>

    <polygon class="card-front" fill="url(#front-fill)"
      points="307.5,381.6 573.8,113.4 600,140.6 600,151.9 611.3,164 622.5,151.9 622.5,140.6 648.8,113.4 919.7,381.6"/>

    <polygon class="card-back-band" fill="url(#band-fill)"
      points="307.5,676 328.5,654.5 898.7,654.5 919.7,676"/>
    <polygon class="card-back" fill="url(#back-fill)"
      points="328.5,654.5 573.8,407.8 600,435 600,446.3 611.3,458.4 622.5,446.3 622.5,435 648.8,407.8 898.7,654.5"/>

    <g class="icon-address" transform="translate(541,570)">
      <rect x="-7" y="-7" width="14" height="14" fill="var(--ink-white)" transform="rotate(45)"/>
      <path d="M-4,0.5 L0,-3.5 L4,0.5 L2.8,0.5 L2.8,3.5 L-2.8,3.5 L-2.8,0.5 Z" fill="var(--blue-mid)"/>
    </g>
    <g class="icon-phone" transform="translate(559,614)">
      <rect x="-7" y="-7" width="14" height="14" fill="var(--ink-white)" transform="rotate(45)"/>
      <path d="M-3,-3.5 Q-4,0.5 -0.5,3 Q2,4.5 3.5,3 L2,1.2 L0.6,1.8 Q-1.4,0.6 -1.6,-1.2 L-0.8,-2.2 Z" fill="var(--blue-mid)"/>
    </g>
  </svg>

  <div class="text company-name">Northvale</div>
  <div class="text company-sub">Realty Management Corporation</div>

  <div class="text person-name">Tariq Hamdan</div>
  <div class="text person-title">PRESIDENT</div>

  <div class="text contact-block address">
    3187 Thornwick Avenue<br>
    Suite C<br>
    Harlow Springs, WI 60152
  </div>
  <div class="text contact-block phones">
    Phone 630.417.2286<br>
    Fax 630.417.2287<br>
    Cell 630.473.8062
  </div>

  <div class="text email">vantorp@mailbreeze.net</div>
</body>
</html>
```